Need CATCHY/VIVID Banner design for my new UTV/ATV/Off Road Vehicle turn signal/lighting company

I need a banner ad designed so I can advertise on several different ATV (all terrain vehicle), UTV (Utility Vehicles), Golf Cart and Off-Road Vehicle forums. Ads need to be very catchy and produce a call to action. Action is getting hits to my website. Our main business is selling turn signal kits to make your side by side or your ATV/UTV street legal, as some states now allow you to drive these on public roads if you have the following items: Turn Signals, Horn, Lighted license plate bracket, headlights and brake lights. We sell all of these items for just about any model vehicle out there. Our call to action for this banner would be to get more website visits.

Target Market(s)

Off-road/outdoor enthusiasts,

Industry/Entity Type

Car Accessorie

Font styles to use
Sans Serif

Requirements
Must have
• Ad size need to be either 728x90 or 300x250. Colorful ad with an off-road vehicle integrated to the design (think UTV, side-by-side, etc.
Nice to have
• Nice to haves would be anything that makes this banner ad stand out on very boring web pages.
Should not have
• anything dull

```html
<!DOCTYPE html>
<html lang="en">
<head>
<meta charset="UTF-8">
<title>Trailready Signal Kits – Street Legal Off-Road Banner</title>
<link href="https://fonts.googleapis.com/css2?family=Oswald:wght@500;600;700&display=swap" rel="stylesheet">
<style>
  :root {
    --ink: #0d0d0d;
    --white: #ffffff;
    --yellow: #f7c90f;
    --yellow-deep: #f2b705;
    --red: #e3202a;
    --sky: #b7c7d4;
    --haze: #d8d2c4;
    --sand-light: #dcc4a2;
    --sand: #c19a6b;
    --earth: #8a6a48;
    --frame-red: #b8312a;
  }
  * { margin: 0; padding: 0; box-sizing: border-box; }
  html, body { width: 1200px; height: 1000px; overflow: hidden; background: var(--white); }
  .banner {
    position: relative;
    width: 1200px;
    height: 1000px;
    overflow: hidden;
    font-family: "Oswald", "Arial Narrow", sans-serif;
  }
  .scene-photo {
    position: absolute; inset: 0;
    background:
      linear-gradient(135deg, rgba(184,49,42,0) 38%, rgba(184,49,42,0.35) 52%, rgba(60,45,40,0.35) 66%, rgba(60,45,40,0) 80%),
      linear-gradient(180deg, var(--sky) 0%, var(--haze) 12%, var(--sand-light) 26%, var(--sand) 55%, var(--earth) 100%);
  }
  .paint-splash {
    position: absolute; inset: 0;
    background:
      radial-gradient(ellipse 700px 420px at 120px 1000px, var(--yellow) 0%, var(--yellow) 45%, rgba(247,201,15,0) 100%),
      radial-gradient(ellipse 560px 300px at 1100px 1000px, var(--yellow-deep) 0%, rgba(242,183,5,0.9) 40%, rgba(242,183,5,0) 100%),
      radial-gradient(ellipse 360px 240px at 60px 640px, rgba(247,201,15,0.85) 0%, rgba(247,201,15,0) 100%),
      radial-gradient(ellipse 260px 160px at 180px 40px, rgba(247,201,15,0.7) 0%, rgba(247,201,15,0) 100%),
      radial-gradient(ellipse 200px 140px at 1180px 160px, rgba(247,201,15,0.6) 0%, rgba(247,201,15,0) 100%);
  }
  .brand {
    position: absolute;
    top: 32px; left: 60px;
    display: flex; align-items: center; gap: 14px;
  }
  .brand-mark { width: 46px; height: 46px; background: var(--red); }
  .brand-name {
    color: var(--white);
    font-weight: 600;
    font-size: 30px;
    letter-spacing: 1px;
    line-height: 1;
  }
  .panel {
    position: absolute; left: 0; top: 0;
    width: 1200px; height: 1000px;
  }
  .headline {
    position: absolute;
    left: 80px; top: 494px;
    width: 800px;
    text-align: center;
    color: var(--white);
    font-weight: 700;
    font-size: 70px;
    line-height: 92px;
    letter-spacing: 1px;
    transform: skewX(-6deg);
  }
  .headline .accent-yellow { color: var(--yellow); }
  .headline .accent-red { color: var(--red); display: block; }
  .divider {
    position: absolute;
    left: 440px; top: 792px;
    width: 150px; height: 3px;
    background: var(--red);
  }
  .feature-list {
    position: absolute;
    left: 64px; top: 814px;
    width: 800px;
    text-align: center;
    color: var(--white);
    font-weight: 500;
    font-size: 22px;
    line-height: 44px;
    letter-spacing: 2px;
    transform: skewX(-6deg);
  }
  .feature-list .dot { color: var(--yellow); padding: 0 14px; }
  .cta {
    position: absolute;
    left: 770px; top: 714px;
    width: 390px; height: 108px;
    display: flex; align-items: center; justify-content: center;
    color: var(--white);
    font-weight: 700;
    font-size: 38px;
    letter-spacing: 1px;
    text-decoration: none;
  }
  .cta svg { position: absolute; inset: 0; z-index: 0; }
  .cta span { position: relative; z-index: 1; transform: skewX(-6deg); margin-top: -8px; }
</style>
</head>
<body>
  <main class="banner">
    <div class="scene-photo" role="img" aria-label="Red side-by-side UTV climbing rocky desert hills under a pale sky"></div>
    <div class="paint-splash" role="img" aria-label="Bright yellow paint splatter across the edges"></div>

    <div class="brand">
      <div class="brand-mark"></div>
      <div class="brand-name">TRAILREADY SIGNAL KITS</div>
    </div>

    <svg class="panel" viewBox="0 0 1200 1000" aria-hidden="true">
      <polygon points="82,468 920,468 884,940 44,940" fill="#0d0d0d"/>
    </svg>

    <h1 class="headline">
      EVERYTHING YOU NEED<br>
      TO GET YOUR <span class="accent-yellow">OFF-ROAD</span>
      <span class="accent-red">ON THE ROAD</span>
    </h1>

    <div class="divider"></div>

    <p class="feature-list">
      TURN SIGNALS<span class="dot">•</span>HORN<span class="dot">•</span>BRAKE LIGHTS<br>
      HEADLIGHTS<span class="dot">•</span>LIGHTED LICENSE PLATE FRAME
    </p>

    <a class="cta" href="#shop">
      <svg viewBox="0 0 390 108" aria-hidden="true">
        <polygon points="30,8 390,8 372,108 12,108" fill="#ffffff"/>
        <polygon points="18,0 378,0 360,98 0,98" fill="#e3202a"/>
      </svg>
      <span>SHOP NOW</span>
    </a>
  </main>
</body>
</html>
```